Report Design

I am looking for a redesign of our monthly inspection reports we submit to our customers. I uploaded the current one we use (Tallowfern) and also that of a competitor (Cedar Knoll). I want to more copy the layout of the Cedarknoll report I attached but with more flow and design.

Requirements
Must have
• This has to be in a template format that we can modify the content every month.

```html
<!DOCTYPE html>
<html lang="en">
<head>
<meta charset="utf-8">
<title>Landscape, Irr. &amp; Property Inspection – Page 3</title>
<link href="https://fonts.googleapis.com/css2?family=Saira+Semi+Condensed:wght@600;700&family=Dosis:wght@500;600&display=swap" rel="stylesheet">
<style>
  :root {
    --green-dark: #006934;
    --green-light: #52c44a;
    --ink: #111111;
    --paper: #ffffff;
    --rule: #1c7a3e;
  }
  * { margin: 0; padding: 0; box-sizing: border-box; }
  html, body { width: 848px; height: 1200px; overflow: hidden; background: var(--paper); }
  body { position: relative; font-family: "Dosis", sans-serif; color: var(--ink); }

  .report-title {
    position: absolute; left: 50px; top: 52px;
    font-family: "Saira Semi Condensed", sans-serif; font-weight: 700;
    font-size: 24px; letter-spacing: -0.2px;
  }
  .site-bar {
    position: absolute; left: 50px; top: 94px; width: 689px; height: 53px;
    background: var(--green-dark); color: #fff;
    font-family: "Saira Semi Condensed", sans-serif; font-weight: 700;
    font-size: 25px; line-height: 53px; padding-left: 13px;
  }
  .page-number {
    position: absolute; left: 755px; top: 94px; width: 51px; height: 53px;
    background: var(--green-light); color: #fff; text-align: center;
    font-family: "Saira Semi Condensed", sans-serif; font-weight: 700;
    font-size: 24px; line-height: 53px;
  }

  .item {
    position: absolute; border: 1.3px solid var(--rule);
  }
  .item-heading {
    position: absolute; left: 23px;
    font-family: "Saira Semi Condensed", sans-serif; font-weight: 700;
    font-size: 18px; color: var(--green-dark);
  }
  .item-heading .num { display: inline-block; width: 26px; }
  .item-note {
    position: absolute; left: 23px; font-size: 15px; line-height: 19px; font-weight: 500;
  }
  .photo { position: absolute; }
  .photo.bed-curb { background: linear-gradient(180deg, #b9c4b0 0%, #3e5a2c 35%, #4a3a2c 60%, #a8a8a6 85%); }
  .photo.bed-wall { background: linear-gradient(160deg, #e4dccb 0%, #3d5d2a 40%, #5b4a36 65%, #7ea84a 100%); }
  .photo.bed-washed { background: linear-gradient(170deg, #ddd8cc 0%, #b8aa96 45%, #6c5c48 70%, #8a8a88 100%); }
  .photo.bed-palms { background: linear-gradient(180deg, #e6dccb 0%, #4f6e36 40%, #2f4a24 62%, #a6a6a4 100%); }

  .footer-rule { position: absolute; left: 50px; top: 1082px; width: 757px; height: 1.5px; background: var(--rule); }
  .footer-title {
    position: absolute; left: 61px; top: 1100px;
    font-family: "Saira Semi Condensed", sans-serif; font-weight: 700; font-size: 21px;
  }
  .footer-division { position: absolute; left: 61px; top: 1130px; font-size: 15.5px; color: var(--green-dark); font-weight: 500; }
  .footer-contacts { position: absolute; left: 63px; top: 1157px; display: flex; gap: 22px; font-size: 13.5px; font-weight: 500; }
  .contact { display: flex; align-items: center; gap: 7px; }
  .contact svg { width: 13px; height: 13px; }

  .brand { position: absolute; left: 668px; top: 1128px; width: 136px; text-align: center; }
  .brand-name {
    display: flex; align-items: center; justify-content: center; gap: 5px;
    font-family: "Saira Semi Condensed", sans-serif; font-weight: 700; font-size: 22px; color: var(--ink);
  }
  .brand-name .mark { width: 10px; height: 10px; background: var(--green-dark); }
  .brand-tag { font-size: 9.5px; font-weight: 600; margin-top: 1px; }
</style>
</head>
<body>
  <h1 class="report-title">Landscape, Irr. &amp; Property Inspection</h1>
  <div class="site-bar">Gardens on Larkmoor POA &amp; Retail</div>
  <div class="page-number">3</div>

  <section class="item" style="left:50px; top:170px; width:755px; height:426px;">
    <h2 class="item-heading" style="top:26px;"><span class="num">5.</span>Fill in Coonties:</h2>
    <p class="item-note" style="top:57px;">Coonties need to be filled in here. As well as side of Bun Barn.</p>
    <div class="photo bed-curb" role="img" aria-label="Planting island by parking spaces with coontie gaps in the mulch" style="left:22px; top:103px; width:340px; height:292px;"></div>
    <div class="photo bed-wall" role="img" aria-label="Bed beside building wall with browned coonties near a sign post" style="left:389px; top:103px; width:340px; height:292px;"></div>
  </section>

  <section class="item" style="left:50px; top:615px; width:379px; height:444px;">
    <h2 class="item-heading" style="top:21px;"><span class="num">6.</span>Mulch:</h2>
    <p class="item-note" style="top:52px; width:336px; text-align:justify;">Overall the place could use fresh mulch, or we could just mulch these washed out areas that are an eye sore.</p>
    <div class="photo bed-washed" role="img" aria-label="Washed out bed along a wall with exposed soil and ornamental grasses" style="left:22px; top:121px; width:340px; height:291px;"></div>
  </section>

  <section class="item" style="left:428px; top:616px; width:377px; height:443px;">
    <h2 class="item-heading" style="top:21px;"><span class="num">7.</span>Pruning:</h2>
    <p class="item-note" style="top:51px;">All the little palms have been pruned up to look clean</p>
    <div class="photo bed-palms" role="img" aria-label="Pruned small palms in a narrow bed beside a building service lane" style="left:14px; top:120px; width:347px; height:291px;"></div>
  </section>

  <div class="footer-rule"></div>
  <div class="footer-title">Landscape, Irr. &amp; Property Inspection</div>
  <div class="footer-division">Landscape and Grounds Maintenance Division</div>
  <div class="footer-contacts">
    <span class="contact">
      <svg viewBox="0 0 14 14"><circle cx="7" cy="7" r="7" fill="#111"/><path d="M4.5 3.5l1.5 0 .6 1.8-1 .7a5 5 0 0 0 2.4 2.4l.7-1 1.8.6v1.5c0 .5-.5.9-1 .8A6.5 6.5 0 0 1 3.7 4.5c-.1-.5.3-1 .8-1z" fill="#fff"/></svg>
      555-014-2380
    </span>
    <span class="contact">
      <svg viewBox="0 0 14 14"><circle cx="7" cy="7" r="7" fill="#111"/><rect x="4" y="5.5" width="6" height="4" fill="#fff"/><rect x="5" y="3.5" width="4" height="2" fill="#fff"/></svg>
      Fax 555-019-7712
    </span>
    <span class="contact">
      <svg viewBox="0 0 14 14"><circle cx="7" cy="7" r="7" fill="#111"/><path d="M7 3a2.3 2.3 0 0 0-2.3 2.3C4.7 7 7 9.5 7 9.5S9.3 7 9.3 5.3A2.3 2.3 0 0 0 7 3z" fill="#fff"/><rect x="4" y="10" width="6" height="1" fill="#fff"/></svg>
      4120 Quarry Hollow Road, Fernvale, FL 30000
    </span>
  </div>

  <div class="brand">
    <div class="brand-name"><span class="mark"></span>Tallowfern</div>
    <div class="brand-tag">Landscape and Maintenance, Inc.</div>
  </div>
</body>
</html>
```